Award-winnning Estate Agent needs a premium version of their 'For Sale' board design

We need a premium option for our 'For Sale' board design. We have a standard board that is attached to this brief, but were are looking to have a premium design version that we will use when selling exclusive properties. Our company name is Harbour Lane Estates and the name for this is exclusive selection is: 'The Harbour Collection'. The design needs to work with our current brand, but have a distinctive PREMIUM feel to it. I have uploaded the barnd guidelines and also some of the exisisting logo variations. We do NOT need a new logo but feel free to play around with colours, fonts, sizes etc. for the sign.

Target Market(s)

Property buyers & house hunters

Industry/Entity Type

Real Estate - Residential Property

Font styles to use
Sans Serif

Requirements
Must have
• A premium fee, must be square design, must be easy to read when driving past the sign
Nice to have
• I'm open ot ideas

```html
<!DOCTYPE html>
<html lang="en">
<head>
<meta charset="utf-8">
<title>Harbour Lane Estates – For Sale</title>
<link rel="stylesheet" href="https://fonts.googleapis.com/css2?family=Arimo:ital,wght@0,700;1,700&display=swap">
<style>
  :root {
    --board-black: #000000;
    --text-white: #ffffff;
    --gold-deep: #c8962e;
    --gold-bright: #f7c52a;
    --gold-pale: #fdf6c8;
    --gold-mid: #e3b74a;
    --gold-sheen: linear-gradient(90deg, #f7c52a 0%, #fbe38a 22%, #c8962e 45%, #f3dc8c 62%, #fffbe0 80%, #fdf3c0 100%);
  }
  html, body {
    margin: 0;
    padding: 0;
    overflow: hidden;
    background: var(--board-black);
  }
  .board {
    position: relative;
    width: 1200px;
    height: 1200px;
    background: var(--board-black);
    font-family: "Arimo", Arial, sans-serif;
    overflow: hidden;
  }
  .flourish {
    position: absolute;
    background: var(--gold-sheen);
    border-radius: 14px;
    opacity: 0.85;
  }
  .flourish--tl-row { left: 58px; top: 55px; width: 236px; height: 32px; }
  .flourish--tl-col { left: 60px; top: 105px; width: 34px; height: 200px; }
  .flourish--tr-row { left: 906px; top: 55px; width: 236px; height: 32px; }
  .flourish--tr-col { left: 1106px; top: 105px; width: 34px; height: 200px; }
  .flourish--divider-top { left: 510px; top: 522px; width: 180px; height: 31px; }
  .flourish--divider-bottom { left: 510px; top: 638px; width: 180px; height: 31px; }

  .brand-mark {
    position: absolute;
    left: 540px;
    top: 220px;
    width: 120px;
    height: 120px;
    background: var(--text-white);
  }
  .brand-name {
    position: absolute;
    left: 0;
    top: 392px;
    width: 1200px;
    text-align: center;
    color: var(--text-white);
    font-weight: 700;
    font-size: 66px;
    line-height: 1;
    margin: 0;
  }
  .rule {
    position: absolute;
    height: 2px;
    background: var(--text-white);
  }
  .rule--top-left { left: 62px; top: 536px; width: 438px; }
  .rule--top-right { left: 700px; top: 536px; width: 438px; }
  .rule--bottom-left { left: 62px; top: 652px; width: 438px; }
  .rule--bottom-right { left: 700px; top: 652px; width: 438px; }

  .collection-name {
    position: absolute;
    left: 0;
    top: 561px;
    width: 1200px;
    text-align: center;
    color: var(--text-white);
    font-style: italic;
    font-weight: 700;
    font-size: 68px;
    line-height: 1;
    margin: 0;
  }
  .sale-headline {
    position: absolute;
    left: 0;
    top: 682px;
    width: 1200px;
    text-align: center;
    font-weight: 700;
    font-size: 224px;
    line-height: 1;
    letter-spacing: 2px;
    margin: 0;
    background: var(--gold-sheen);
    -webkit-background-clip: text;
    background-clip: text;
    color: transparent;
  }
  .phone {
    position: absolute;
    left: 0;
    top: 880px;
    width: 1200px;
    text-align: center;
    color: var(--text-white);
    font-weight: 700;
    font-size: 166px;
    line-height: 1;
    margin: 0;
  }
  .web-band {
    position: absolute;
    left: 0;
    top: 1066px;
    width: 1200px;
    height: 134px;
    background: var(--gold-sheen);
    display: flex;
    align-items: center;
    justify-content: center;
  }
  .web-address {
    color: var(--board-black);
    font-weight: 700;
    font-size: 74px;
    line-height: 1;
    margin: 0 0 8px;
  }
</style>
</head>
<body>
<main class="board">
  <div class="flourish flourish--tl-row" role="img" aria-label="Gold leaf ornament border, top left"></div>
  <div class="flourish flourish--tl-col" role="img" aria-label="Gold leaf ornament border, left side"></div>
  <div class="flourish flourish--tr-row" role="img" aria-label="Gold leaf ornament border, top right"></div>
  <div class="flourish flourish--tr-col" role="img" aria-label="Gold leaf ornament border, right side"></div>

  <div class="brand-mark" aria-hidden="true"></div>
  <h1 class="brand-name">Harbour Lane Estates</h1>

  <div class="rule rule--top-left"></div>
  <div class="rule rule--top-right"></div>
  <div class="flourish flourish--divider-top" role="img" aria-label="Gold leaf divider ornament"></div>

  <h2 class="collection-name">The Harbour Collection</h2>

  <div class="rule rule--bottom-left"></div>
  <div class="rule rule--bottom-right"></div>
  <div class="flourish flourish--divider-bottom" role="img" aria-label="Gold leaf divider ornament"></div>

  <p class="sale-headline">FOR SALE</p>
  <p class="phone">01632 960418</p>

  <div class="web-band">
    <p class="web-address">www.harbourlaneestates.co.uk</p>
  </div>
</main>
</body>
</html>
```